Vesk Architecture

We are a architectural design and build company working between scales 1/1000 to 1/1 we want people to understand our difference from our design experience and quality.we build hotels restourants and office spaces.Our company name is Vesk architecture to mind sustainability.

We want to write our adress phone and work spesifications on the card and we want our logo as backround.

Ps:you could find the logo adress and phone box numbers from the web:www.veskmimarlik-ornek.com

Target Market(s)

Who looks for experts.

Industry/Entity Type

Architecture

Requirements
Must have
• Design is over everything.
Should not have
• we don want it to be colorfull

```html
<!DOCTYPE html>
<html lang="tr">
<head>
<meta charset="utf-8">
<title>Vesk Mimarlık – Business Card</title>
<link rel="stylesheet" href="https://fonts.googleapis.com/css2?family=Arimo:wght@400&display=swap">
<style>
  :root {
    --page: #ffffff;
    --card: #0b0d0d;
    --ink: #dcdcdc;
    --ghost: #161818;
  }
  html, body {
    margin: 0;
    padding: 0;
    width: 1200px;
    height: 434px;
    overflow: hidden;
    background: var(--page);
    font-family: "Arimo", Arial, sans-serif;
  }
  .sheet {
    position: relative;
    width: 1200px;
    height: 434px;
  }
  .card {
    position: absolute;
    top: 69px;
    height: 317px;
    background: var(--card);
    overflow: hidden;
  }
  .card--front { left: 50px; width: 542px; }
  .card--back  { left: 615px; width: 543px; }

  .brand-name {
    position: absolute;
    right: 18px;
    bottom: 14px;
    margin: 0;
    color: var(--ink);
    font-weight: 400;
    font-size: 84px;
    line-height: 1;
    letter-spacing: 1px;
  }

  .brand-ghost {
    position: absolute;
    left: 10px;
    top: 20px;
    margin: 0;
    color: var(--ghost);
    font-weight: 400;
    font-size: 250px;
    line-height: 1;
    white-space: nowrap;
  }

  .contact {
    position: absolute;
    right: 30px;
    color: var(--ink);
    font-size: 14px;
    line-height: 1;
    text-align: right;
    white-space: nowrap;
    margin: 0;
  }
  .contact--person  { top: 118px; right: 30px; }
  .contact--street  { top: 195px; right: 26px; }
  .contact--city    { top: 225px; right: 26px; }
  .contact--lines   { top: 256px; right: 30px; }
</style>
</head>
<body>
  <main class="sheet">
    <section class="card card--front" aria-label="Card front">
      <h1 class="brand-name">Vesk</h1>
    </section>

    <section class="card card--back" aria-label="Card back">
      <p class="brand-ghost" aria-hidden="true">Vesk</p>
      <p class="contact contact--person">Deniz Arat KAYA - Mimar</p>
      <p class="contact contact--street">Yelken Mah. Liman Cad. Ada Sok.</p>
      <p class="contact contact--city">No : 7 Kumsal / ISTANBUL</p>
      <p class="contact contact--lines">t. 0000 555 01 23 f. 0000 555 01 24 e.veskmimarlik@ornek.com</p>
    </section>
  </main>
</body>
</html>
```